Hollow Fern Kentucky Bourbon Whiskey

We need a label design for a bottle of whiskey. It is for a 750 ml bottle and needs to have a place to write in proof, age, and bottle number at bottom of label. It is a single barrel bourbon. We want to include our tree logo attached in the upload files in some way. Leave out the Distillery part to where it just says Hollow Fern Bourbon Whiskey with the tree. We need the label to be clean and modern. I have also attached a picture of the bottle the label is intended to go on.

Industry/Entity Type

Bourbon

Requirements
Must have
• Hollow Fern tree from file

```html
<!DOCTYPE html>
<html lang="en">
<head>
<meta charset="utf-8">
<title>Hollow Fern Bourbon Whiskey — Label</title>
<link href="https://fonts.googleapis.com/css2?family=Cinzel:wght@400;600;700&family=Crimson+Text&family=Rye&display=swap" rel="stylesheet">
<style>
  :root {
    --page: #ffffff;
    --label-black: #0a0a0a;
    --field: #1c1c1c;
    --gold: #b8952a;
    --gold-light: #d9b960;
    --white: #f4f4f2;
    --cream: #e2dbd0;
    --ink: #2a2522;
  }
  html, body {
    margin: 0;
    padding: 0;
    width: 1200px;
    height: 1200px;
    overflow: hidden;
    background: var(--page);
  }
  .label-canvas { display: block; width: 1200px; height: 1200px; }
  .outer-frame { fill: var(--label-black); }
  .gold-rule { fill: none; stroke: var(--gold); stroke-width: 4; }
  .field { fill: var(--field); stroke: var(--gold); stroke-width: 1.5; }
  .ornament { fill: var(--gold); opacity: 0.35; }
  .brand-mark { fill: var(--gold); }
  .brand-name { font-family: "Cinzel", serif; font-weight: 600; fill: var(--white); font-size: 44px; }
  .spirit-type { font-family: "Cinzel", serif; font-weight: 400; fill: var(--white); font-size: 45px; }
  .spirit-name { font-family: "Rye", serif; fill: var(--white); font-size: 92px; }
  .info-card { fill: var(--cream); }
  .info-edge { fill: var(--field); }
  .info-rule { stroke: var(--ink); stroke-width: 1.2; }
  .field-label { font-family: "Crimson Text", serif; font-size: 15px; fill: var(--ink); }
  .fact { font-family: "Rye", serif; font-size: 19px; fill: var(--ink); }
  .fact-center { font-family: "Cinzel", serif; font-weight: 700; font-size: 13px; fill: var(--ink); }
</style>
</head>
<body>
<svg class="label-canvas" viewBox="0 0 1200 1200" xmlns="http://www.w3.org/2000/svg">
  <defs>
    <linearGradient id="band-glow" x1="0" x2="1" y1="0" y2="0">
      <stop offset="0" stop-color="#d9b960" stop-opacity="0"/>
      <stop offset="0.5" stop-color="#d9b960" stop-opacity="0.35"/>
      <stop offset="1" stop-color="#d9b960" stop-opacity="0"/>
    </linearGradient>
    <pattern id="serration" width="6" height="6" patternUnits="userSpaceOnUse">
      <polygon points="0,0 6,0 3,4"/>
    </pattern>
  </defs>

  <!-- Label frame -->
  <polygon class="outer-frame" points="263,275 937,275 902,924 298,924"/>
  <polygon class="gold-rule" points="276,287 924,287 891,912 309,912"/>
  <polygon class="field" points="294,300 906,300 875,899 325,899"/>

  <!-- Corner flourishes -->
  <rect class="ornament" x="307" y="319" width="110" height="131" rx="40" role="img" aria-label="Gold corner flourish, top left"/>
  <rect class="ornament" x="781" y="319" width="111" height="131" rx="40" role="img" aria-label="Gold corner flourish, top right"/>
  <rect class="ornament" x="330" y="707" width="60" height="41" rx="16" role="img" aria-label="Small gold flourish, lower left"/>
  <rect class="ornament" x="809" y="707" width="60" height="41" rx="16" role="img" aria-label="Small gold flourish, lower right"/>

  <!-- Brand -->
  <circle class="brand-mark" cx="600" cy="405" r="36"/>
  <text class="brand-name" x="600" y="502" text-anchor="middle" textLength="393" lengthAdjust="spacingAndGlyphs">HOLLOW FERN</text>

  <!-- Spirit type band -->
  <rect x="450" y="573" width="298" height="62" fill="url(#band-glow)"/>
  <line x1="470" y1="576" x2="730" y2="576" stroke="var(--gold-light)" stroke-opacity="0.5" stroke-width="1"/>
  <line x1="470" y1="633" x2="730" y2="633" stroke="var(--gold-light)" stroke-opacity="0.5" stroke-width="1"/>
  <text class="spirit-type" x="600" y="622" text-anchor="middle" textLength="227" lengthAdjust="spacingAndGlyphs">BOURBON</text>

  <text class="spirit-name" x="601" y="739" text-anchor="middle" textLength="348" lengthAdjust="spacingAndGlyphs">WHISKEY</text>

  <!-- Bottle details card -->
  <g class="details">
    <rect class="info-card" x="374" y="776" width="443" height="106"/>
    <rect x="374" y="776" width="443" height="5" fill="url(#serration)" class="info-edge"/>
    <rect x="374" y="877" width="443" height="5" fill="url(#serration)" class="info-edge" transform="rotate(180 595.5 879.5)"/>

    <line class="info-rule" x1="395" y1="795" x2="795" y2="795"/>
    <line class="info-rule" x1="395" y1="834" x2="795" y2="834"/>
    <line class="info-rule" x1="525" y1="806" x2="525" y2="826"/>
    <line class="info-rule" x1="665" y1="806" x2="665" y2="826"/>
    <text class="field-label" x="403" y="811">Proof</text>
    <text class="field-label" x="533" y="811">Bottle No.</text>
    <text class="field-label" x="676" y="811">Age</text>

    <line class="info-rule" x1="511" y1="841" x2="511" y2="860"/>
    <line class="info-rule" x1="680" y1="841" x2="680" y2="860"/>
    <text class="fact" x="404" y="861" textLength="59" lengthAdjust="spacingAndGlyphs">750 ML</text>
    <text class="fact-center" x="540" y="858" textLength="112" lengthAdjust="spacingAndGlyphs">HAND CRAFTED</text>
    <text class="fact" x="700" y="861" textLength="101" lengthAdjust="spacingAndGlyphs">45% ALC./VOL</text>
  </g>
</svg>
</body>
</html>
```